Zielgruppe
wir sind eine Sicherheitsunternehmen und suchen ein ausgefallenes Design um alle Privathaushalte sowohl auch kleine und große Firmen zu beindrucken.
Aufgabenstellung
Die Firma möchte das erste Sicherheitsunternehmen sein was absolut Nachhaltig, ökologisch und umweltfreundlich arbeitet. Die Natur, der Klimawechsel steht im absoluten Vordergrund. Wir möchten zeigen das man auch als Dienstleister im Sicheheitsbereich im Einklang mit der Umwelt sein kann. und mit diesem Konzept möchten wir an die Bevölkerung rantreten. Das Motto: mit uns als Partner werden Fremdfirmen mehr Kunden gewinnen, da wir umweltbewusst und mit den uns verfügbaren Ressourcen sehr ökologisch und grün sind. Das Design sollte bitte nicht in schrillen Farben dargestellt werden. Das Logo und unsere Grundfarben sind Schwarz/ Antrazith/ Weiss/Creme und Naturrholzfarben.

```html
<!DOCTYPE html>
<html lang="de">
<head>
<meta charset="utf-8">
<title>Lumen Sicherheit – Broschüre</title>
<link href="https://fonts.googleapis.com/css2?family=Roboto:wght@300;400;700&display=swap" rel="stylesheet">
<style>
:root{
  --stage:#f4f4f4;
  --gold:#b38f55;
  --gold-light:#d8c4a0;
  --cream:#fbeecf;
  --ink:#333333;
  --ink-soft:#4a4a4a;
  --brand-ink:#151515;
  --white:#ffffff;
  --rule:#d9c29a;
}
*{margin:0;padding:0;box-sizing:border-box}
html,body{width:765px;height:1200px;overflow:hidden;background:var(--stage);font-family:'Roboto',Arial,sans-serif;color:var(--ink)}
.page{position:absolute;background:var(--white);box-shadow:0 1px 2px rgba(0,0,0,.18);overflow:hidden}
.page svg.shapes{position:absolute;left:0;top:0}
.abs{position:absolute}
.cover{left:260px;top:53px;width:245px;height:245px}
.about{left:138px;top:326px;width:488px;height:244px}
.services{left:138px;top:599px;width:488px;height:244px}
.back{left:260px;top:872px;width:245px;height:245px}

.cover-title{left:13px;top:21px;font-weight:700;font-size:18px;line-height:23px;letter-spacing:.2px}
.cover-title .dark{color:var(--ink-soft)}
.cover-title .light{color:var(--white)}
.cover-band{left:0;top:210px;width:245px;height:35px;background:var(--cream)}
.cover-url{left:0;top:225px;width:245px;text-align:center;font-size:5px;font-weight:700;letter-spacing:.6px;color:var(--ink)}

.brand{display:flex;align-items:center;gap:4px}
.brand-square{width:15px;height:15px;border:1.4px solid var(--brand-ink);flex:none}
.brand-name{font-weight:700;font-size:5.6px;line-height:7px;letter-spacing:.4px;color:var(--brand-ink);white-space:nowrap}
.cover-brand{left:8px;top:172px}
.back-brand{left:140px;top:36px}

.about-icon{left:18px;top:120px}
.about-claim{left:19px;top:148px;color:var(--white);font-weight:700;font-size:9.5px;line-height:10px}
.section-title{font-weight:700;color:var(--ink);letter-spacing:.2px;line-height:1}
.about-title{left:309px;top:33px;font-size:16.5px}
.about-rule{left:309px;top:52px;width:164px;height:.6px;background:var(--rule)}
.body-text{font-weight:300;font-size:4.4px;line-height:7px;color:var(--ink-soft)}
.about-text{left:309px;top:91px;width:142px}

.obj-title{left:70px;top:16px;font-size:17px}
.short-rule{height:.6px;width:44px;background:var(--rule)}
.obj-rule{left:70px;top:33px}
.list{font-weight:300;font-size:4.4px;line-height:5.8px;color:var(--ink-soft);list-style:none;white-space:nowrap}
.obj-list-a{left:70px;top:196px}
.obj-list-b{left:140px;top:196px}
.event-title{left:255px;top:163px;font-size:10.5px;line-height:12.5px}
.event-rule{left:255px;top:190px}
.event-list{left:255px;top:196px}
.werk-title{left:379px;top:37px;font-size:10.5px}
.werk-rule{left:379px;top:50px}
.werk-list{left:379px;top:63px}

.contact{left:156px;top:67px;font-size:4.3px;line-height:7px;color:var(--ink);border-collapse:collapse}
.contact td{padding-right:6px;white-space:nowrap}
.contact td.val{font-weight:700;text-align:right;padding-right:0}
</style>
</head>
<body>

<section class="page cover">
  <svg class="shapes" width="245" height="210" viewBox="0 0 245 210">
    <defs>
      <linearGradient id="coverPhoto" x1="0" y1="0" x2="1" y2="1">
        <stop offset="0" stop-color="#6e6c6c"/>
        <stop offset=".3" stop-color="#a9a7a5"/>
        <stop offset=".5" stop-color="#d9d7d4"/>
        <stop offset=".68" stop-color="#8c8886"/>
        <stop offset="1" stop-color="#3f3b3a"/>
      </linearGradient>
    </defs>
    <rect width="245" height="210" fill="url(#coverPhoto)" role="img" aria-label="Schwarzweißfoto: Hand übergibt ein Päckchen"/>
    <polygon points="211,0 245,0 245,30 123,210 90,210" fill="#ffffff" opacity=".16"/>
    <polygon points="155,0 211,0 90,210 60,210" fill="#ffffff" opacity=".24"/>
    <polygon points="190,0 245,0 245,210 124,210" fill="#2e2a29" opacity=".28"/>
    <polygon points="0,0 155,0 50,168 0,106" fill="var(--gold)"/>
    <polygon points="0,106 50,168 90,210 0,210" fill="#ffffff"/>
  </svg>
  <h1 class="abs cover-title"><span class="dark">FÜR IHRE</span><br><span class="light">SICHERHEIT</span></h1>
  <div class="abs brand cover-brand"><span class="brand-square"></span><span class="brand-name">LUMEN SICHERHEIT<br>MIRABELL HUTER</span></div>
  <div class="abs cover-band"></div>
  <div class="abs cover-url">www.lumen-schutz.de</div>
</section>

<section class="page about">
  <svg class="shapes" width="245" height="244" viewBox="0 0 245 244">
    <defs>
      <linearGradient id="lockPhoto" x1="0" y1="0" x2="1" y2="1">
        <stop offset="0" stop-color="#d6c7ad"/>
        <stop offset=".35" stop-color="#b89a74"/>
        <stop offset=".55" stop-color="#c78a5c"/>
        <stop offset=".75" stop-color="#8a6346"/>
        <stop offset="1" stop-color="#3c3a4e"/>
      </linearGradient>
    </defs>
    <polygon points="40,0 245,0 245,65 174,190 140,190" fill="url(#lockPhoto)" role="img" aria-label="Foto: Vorhängeschloss an einer Wand"/>
    <polygon points="200,0 245,0 245,65 190,162" fill="#ffffff" opacity=".14"/>
    <polygon points="0,0 64,0 184,210 0,210" fill="var(--gold)"/>
  </svg>
  <svg class="abs about-icon" width="14" height="19" viewBox="0 0 14 19" aria-hidden="true">
    <path d="M3.5 8V5a3.5 3.5 0 0 1 7 0v3" fill="none" stroke="#fff" stroke-width="1"/>
    <rect x="1.5" y="8" width="11" height="9.5" rx="1" fill="none" stroke="#fff" stroke-width="1"/>
    <rect x="3.5" y="11" width="7" height="4" fill="none" stroke="#fff" stroke-width=".7"/>
  </svg>
  <p class="abs about-claim">Lorem ipsum dolor<br>sit amet dolor sit<br>lorem amet ipsum</p>
  <h2 class="abs section-title about-title">ÜBER UNS</h2>
  <div class="abs about-rule"></div>
  <p class="abs body-text about-text">Sicherheit bedeutet für uns Menschen, frei von Angst und Gefahr zu sein und somit Lebensqualität. Mit steigender Kriminalität wächst das Verlangen nach Sicherheit. Wach- und Sicherheitsdienste stellen sich der ständig steigenden Komplexität der Kriminalität und wirken dieser erfolgreich entgegen. Diesbezüglich bietet der Sicherheitsdienst alle erforderlichen Maßnahmen zur Sicherung von Personen, Gebäuden, Einrichtungen und Sachwerten. Wir legen großen Wert auf die Zusammenarbeit mit den Städten und Gemeinden.</p>
</section>

<section class="page services">
  <svg class="shapes" width="488" height="244" viewBox="0 0 488 244">
    <defs>
      <linearGradient id="lobbyPhoto" x1="0" y1="0" x2="1" y2="0.6">
        <stop offset="0" stop-color="#6f5d45"/>
        <stop offset=".3" stop-color="#9a7450"/>
        <stop offset=".5" stop-color="#c47a3e"/>
        <stop offset=".72" stop-color="#a2835e"/>
        <stop offset=".85" stop-color="#3e3a36"/>
        <stop offset="1" stop-color="#8c877e"/>
      </linearGradient>
      <linearGradient id="plantPhoto" x1="0" y1="0" x2="0.4" y2="1">
        <stop offset="0" stop-color="#8d7d72"/>
        <stop offset=".3" stop-color="#ece6dc"/>
        <stop offset=".6" stop-color="#b8b6b2"/>
        <stop offset=".8" stop-color="#4d5458"/>
        <stop offset="1" stop-color="#7fb0ad"/>
      </linearGradient>
      <linearGradient id="concertPhoto" x1="1" y1="0" x2="0.2" y2="1">
        <stop offset="0" stop-color="#f1ecea"/>
        <stop offset=".35" stop-color="#c8aca2"/>
        <stop offset=".65" stop-color="#7d5f56"/>
        <stop offset="1" stop-color="#2c201d"/>
      </linearGradient>
    </defs>
    <polygon points="0,0 25,46 0,46" fill="var(--gold-light)"/>
    <rect x="0" y="46" width="245" height="136" fill="url(#lobbyPhoto)" role="img" aria-label="Foto: Eingangshalle mit Aufzügen und Treppe"/>
    <polygon points="0,46 25,46 103,182 0,182" fill="var(--gold-light)" opacity=".3"/>
    <rect x="245" y="0" width="122" height="147" fill="url(#plantPhoto)" role="img" aria-label="Foto: Industrieanlage mit Kühltürmen"/>
    <polygon points="325,0 367,0 367,75 300,130" fill="#c0825e" opacity=".22"/>
    <polygon points="245,0 280,0 245,60" fill="#ffffff" opacity=".14"/>
    <rect x="367" y="105" width="121" height="139" fill="url(#concertPhoto)" role="img" aria-label="Foto: Publikum bei einem Konzert im Scheinwerferlicht"/>
  </svg>
  <h2 class="abs section-title obj-title">OBJEKTSCHUTZ</h2>
  <div class="abs short-rule obj-rule"></div>
  <ul class="abs list obj-list-a">
    <li>Zeltbewachung</li><li>Bühnenbewachung</li><li>Baustellenbewachung</li><li>Bewachungen jeglicher Art</li><li>Revierkontrollen</li><li>Außenkontrollen</li><li>Innenkontrollen</li>
  </ul>
  <ul class="abs list obj-list-b">
    <li>Standwachen</li><li>Sonderkontrollen in einem gewünschten Intervall</li><li>Verschluß eines Objektes zur gewünschten Zeit</li><li>Aufschluß eines Objektes zu einer gewünschten Zeit</li><li>Das bewachen von Zügen (Zug &gt; Objekt)</li>
  </ul>
  <h2 class="abs section-title event-title">VERANTALTUNGS-<br>SCHUTZ</h2>
  <div class="abs short-rule event-rule"></div>
  <ul class="abs list event-list">
    <li>Konzerte</li><li>Volksfeste</li><li>Flohmärkte</li><li>private Veranstaltungen</li><li>Hochzeiten</li><li>politische Veranstaltungen, ect.</li>
  </ul>
  <h2 class="abs section-title werk-title">WERKSCHUTZ</h2>
  <div class="abs short-rule werk-rule"></div>
  <ul class="abs list werk-list">
    <li>Dienstschichten in Werken und Produktionsstätten</li><li>Pfortendienste</li><li>Nachtdienste mit Rundgängen</li><li>Besetzung einer Sicherheitszentrale</li>
  </ul>
</section>

<section class="page back">
  <svg class="shapes" width="245" height="245" viewBox="0 0 245 245">
    <defs>
      <linearGradient id="backPhoto" x1="0" y1="0" x2="0.8" y2="1">
        <stop offset="0" stop-color="#6e625c"/>
        <stop offset=".3" stop-color="#a59486"/>
        <stop offset=".55" stop-color="#7f6a58"/>
        <stop offset=".8" stop-color="#9a8d84"/>
        <stop offset="1" stop-color="#5e5856"/>
      </linearGradient>
    </defs>
    <rect width="245" height="245" fill="url(#backPhoto)" role="img" aria-label="Foto: Vorhängeschloss an einer Kette, Nahaufnahme"/>
    <polygon points="60,0 92,0 125,55 233,245 198,245" fill="#ffffff" opacity=".16"/>
    <polygon points="92,0 157,0 125,55" fill="var(--gold-light)"/>
    <polygon points="157,0 185,0 245,104 245,245 233,245 125,55" fill="#ffffff"/>
    <polygon points="185,0 245,0 245,104" fill="var(--gold)"/>
  </svg>
  <div class="abs brand back-brand"><span class="brand-square"></span><span class="brand-name">LUMEN SICHERHEIT<br>MIRABELL HUTER</span></div>
  <table class="abs contact">
    <tr><td>Tel.</td><td class="val">0176 12 34 5678</td></tr>
    <tr><td>E-Mail</td><td class="val">info@lumen-schutz.de</td></tr>
    <tr><td>Web</td><td class="val">www.lumen-schutz.de</td></tr>
  </table>
</section>

</body>
</html>
```